New Album "A night beside the silver hills"

I need a cd cover for a new pop rock album called "A night beside the silver hills"
The main color of the artwork shall obviously be orange. The artwork shouldn't be too "obvious", but it would be better something a bit abstract.
Please remember that it is a Music Cd Cover, so do not send business logo or advertisement images.

Target Market(s)

It's a pop rock album, so the target customers are young and adult people from 15-60 years old

Requirements
Must have
• Orange as main colour
The Artist name is: Remy Castellan
The Title: A night beside the silver hills
Should not have
• Not too cheesy or dreamy images please. No simple sunset or sunrise pics

```html
<!DOCTYPE html>
<html lang="en">
<head>
<meta charset="utf-8">
<title>Remy Castellan – A night beside the silver hills</title>
<link rel="stylesheet" href="https://fonts.googleapis.com/css2?family=Montserrat:wght@600&family=Libre+Baskerville:ital@1&display=swap">
<style>
  :root {
    --backdrop: #5d5d66;
    --sleeve-white: #f3f3f1;
    --sky-light: #3aa7d8;
    --sky-mid: #2391c9;
    --cloud-gold: #f2a735;
    --cloud-orange: #ec7f2b;
    --cloud-red: #d9552a;
    --cloud-deep: #b83e22;
    --type-light: #f6f3ee;
  }
  * { margin: 0; padding: 0; box-sizing: border-box; }
  html, body {
    width: 1200px;
    height: 1000px;
    overflow: hidden;
    background: var(--backdrop);
  }
  .canvas {
    position: relative;
    width: 1200px;
    height: 1000px;
    display: flex;
    align-items: center;
    justify-content: center;
  }
  .album-cover {
    position: relative;
    width: 800px;
    height: 800px;
    background: var(--sleeve-white);
    padding: 26px;
  }
  .cover-artwork {
    position: absolute;
    inset: 26px;
    background: linear-gradient(180deg,
      var(--sky-light) 0%,
      var(--sky-mid) 14%,
      var(--cloud-gold) 30%,
      var(--cloud-orange) 50%,
      var(--cloud-red) 75%,
      var(--cloud-deep) 100%);
  }
  .cover-titles {
    position: absolute;
    left: 26px;
    right: 26px;
    top: 635px;
    text-align: center;
    color: var(--type-light);
  }
  .artist-name {
    font-family: "Montserrat", sans-serif;
    font-weight: 600;
    font-size: 48px;
    letter-spacing: 0.14em;
    line-height: 1;
    text-transform: uppercase;
  }
  .album-title {
    margin-top: 14px;
    font-family: "Libre Baskerville", serif;
    font-style: italic;
    font-size: 29px;
    letter-spacing: 0.03em;
    line-height: 1.1;
  }
</style>
</head>
<body>
  <main class="canvas">
    <section class="album-cover">
      <div class="cover-artwork" role="img" aria-label="Low-poly illustration of large orange faceted clouds filling a blue faceted sky"></div>
      <div class="cover-titles">
        <h1 class="artist-name">Remy Castellan</h1>
        <p class="album-title">a night beside the silver hills</p>
      </div>
    </section>
  </main>
</body>
</html>
```